Toms welding and seed cleaning Business cards

Toms welding and seed cleaningWe clean wheat seed on farm with portable cleaners so the farmers have pure wheat seed to plant back for the next crop. We are certified to clean foundation, registered, and certified seed wheat. Our cleaners being portable make it easier for the farmers because we do it right on there farm so they don't have to haul it all to townWhen there is no wheat to clean we weld in the winter. We improve, add onto, and build new corrals. We also build sheds, cattle shelters, and wind breaks. Other welding is welcomed
Updates

Project Deadline Extended
Reason: I need to extend the deadline because I've been busy and not had my game together. I need more time figure out what I want yet

Industry/Entity Type

Agriculture

Contact Information for Business Card

Just "toms welding and seed cleaning" on front and other info on the back
On the back side I would like to have my address.
Martin Bellard
48903 N COUNTY RD 137
GLENWOOD OK 73612
Phone #5804419163

Font styles to use
Sans Serif

Requirements
Must have
• list we are certified to clean foundation, registered, and certified wheat
• State that they are portable cleaners
• For the welding part list, add on to, improve on, and repair existing corrals and new corrals and other welding welcomed
Nice to have
• A wheat field with some metal corrals on the side with a nice classic looking barn for a background. Maybe some cattle in the corrals
• A nice looking farm yard would be good too

```html
<!DOCTYPE html>
<html lang="en">
<head>
<meta charset="utf-8">
<title>Business card – back side</title>
<link rel="stylesheet" href="https://fonts.googleapis.com/css2?family=Quicksand:wght@300;500;700&family=Share+Tech+Mono&family=Fredoka:wght@600&display=swap">
<style>
  :root {
    --yellow: #f0e93a;
    --yellow-soft: #f6ef5c;
    --white: #ffffff;
    --ink: #111111;
    --green: #2f9a3e;
    --blue-head: #1f7fc0;
    --blue-text: #3aa4de;
    --ribbon: #e4e4e2;
    --bullet: #c9cccc;
  }
  * { margin: 0; padding: 0; box-sizing: border-box; }
  html, body { width: 1200px; height: 702px; overflow: hidden; background: var(--white); }
  .card { position: relative; width: 1200px; height: 702px; background: var(--yellow-soft); overflow: hidden; }

  .card-back-shape { position: absolute; inset: 0; }

  .contact-panel { position: absolute; left: 0; top: 0; width: 600px; height: 702px; background: var(--yellow); }
  .band { position: absolute; left: 0; width: 600px; height: 2px; background: rgba(0,0,0,0.05); box-shadow: 0 3px 6px rgba(0,0,0,0.05); }

  .owner-name {
    position: absolute; left: 0; width: 600px; top: 128px; text-align: center;
    font-family: "Quicksand", sans-serif; font-size: 46px; letter-spacing: 1px; color: var(--ink);
    text-transform: uppercase; line-height: 1;
  }
  .owner-name .first { font-weight: 700; }
  .owner-name .last { font-weight: 300; }
  .name-rule { position: absolute; left: 90px; width: 440px; top: 188px; height: 2px;
    background: linear-gradient(90deg, transparent, rgba(0,0,0,0.18) 30%, rgba(0,0,0,0.18) 70%, transparent); }

  .contact-icon { position: absolute; left: 100px; }
  .contact-text {
    position: absolute; left: 179px; font-family: "Share Tech Mono", monospace; color: var(--green);
    font-size: 21px; letter-spacing: 0.6px; line-height: 29px;
  }
  .phone-number { font-size: 26px; letter-spacing: 1px; }

  .section-ribbon { position: absolute; left: 600px; }
  .section-title {
    position: absolute; font-family: "Fredoka", sans-serif; font-weight: 600; color: var(--blue-head);
    font-size: 33px; letter-spacing: 0.5px; text-transform: uppercase; line-height: 1;
  }
  .service-list { position: absolute; left: 627px; list-style: none;
    font-family: "Quicksand", sans-serif; font-weight: 500; color: var(--blue-text); font-size: 26px; line-height: 29px; }
  .service-list li { position: absolute; left: 0; width: 360px; padding-left: 41px; white-space: nowrap; letter-spacing: 0.3px; }
  .service-list li::before { content: ""; position: absolute; left: 0; top: 9px; width: 15px; height: 13px; background: var(--bullet); }
</style>
</head>
<body>
<div class="card">
  <svg class="card-back-shape" width="1200" height="702" viewBox="0 0 1200 702">
    <polygon points="600,0 1048,0 1181,210 1181,600 1065,680 600,680" fill="var(--white)"/>
  </svg>

  <section class="contact-panel">
    <div class="band" style="top:254px"></div>
    <div class="band" style="top:397px"></div>
    <div class="band" style="top:531px"></div>

    <h1 class="owner-name"><span class="first">Martin</span> <span class="last">Bellard</span></h1>
    <div class="name-rule"></div>

    <svg class="contact-icon" style="top:302px" width="48" height="44" viewBox="0 0 48 44" aria-label="Address">
      <polygon points="24,2 2,22 8,22 24,8 40,22 46,22" fill="var(--green)"/>
      <rect x="34" y="5" width="5" height="10" fill="var(--green)"/>
      <path d="M10 22 L24 10 L38 22 V42 H28 V30 H20 V42 H10 Z" fill="var(--green)"/>
    </svg>
    <p class="contact-text" style="top:298px">48903 N COUNTY RD 137<br>GLENWOOD OK 73612</p>

    <svg class="contact-icon" style="top:446px" width="48" height="36" viewBox="0 0 48 36" aria-label="Phone">
      <path d="M2 12 C2 3 46 3 46 12 L46 16 L36 16 L34 10 C28 8 20 8 14 10 L12 16 L2 16 Z" fill="var(--green)"/>
      <path d="M10 18 L16 12 H32 L38 18 V34 H10 Z" fill="var(--green)"/>
      <circle cx="24" cy="24" r="6" fill="var(--yellow)"/>
      <circle cx="24" cy="24" r="2.5" fill="var(--green)"/>
    </svg>
    <p class="contact-text phone-number" style="top:449px">5804419163</p>
  </section>

  <svg class="section-ribbon" style="top:36px" width="290" height="56" viewBox="0 0 290 56">
    <polygon points="0,0 268,0 286,28 268,56 0,56" fill="var(--ribbon)"/>
  </svg>
  <h2 class="section-title" style="left:644px;top:47px">Welding</h2>
  <ul class="service-list" style="top:0">
    <li style="top:122px">Add on to</li>
    <li style="top:169px">Improve on</li>
    <li style="top:214px">Repair existing<br>corrals</li>
    <li style="top:290px">New corrals and<br>other welding</li>
  </ul>

  <svg class="section-ribbon" style="top:372px" width="290" height="56" viewBox="0 0 290 56">
    <polygon points="0,0 268,0 286,28 268,56 0,56" fill="var(--ribbon)"/>
  </svg>
  <h2 class="section-title" style="left:623px;top:383px">Seed cleaning</h2>
  <ul class="service-list" style="top:0">
    <li style="top:447px">Certified to clean<br>foundation</li>
    <li style="top:530px">Portable cleaners</li>
    <li style="top:586px">Registered and Certified</li>
  </ul>
</div>
</body>
</html>
```